Business cards for law firm with global theme

I'd like business cards with contact info for two offices. They should include the colors and font of the new logo design, which is a stylized globe with an "F" in it. The feel should be very modern and professional.

```html
<!DOCTYPE html>
<html lang="en">
<head>
<meta charset="utf-8">
<title>Marvella Law – Business Cards</title>
<link rel="stylesheet" href="https://fonts.googleapis.com/css2?family=Montserrat:wght@500;600;700&display=swap">
<style>
  :root {
    --backdrop: #03a9e8;
    --navy: #053d6e;
    --sky: #1ab4ee;
    --paper: #fafafa;
    --ink: #1e1e1e;
  }
  * { box-sizing: border-box; margin: 0; padding: 0; }
  html, body { width: 1200px; height: 1200px; overflow: hidden; }
  body {
    background: var(--backdrop);
    font-family: "Montserrat", Arial, sans-serif;
    display: flex;
    flex-direction: column;
    align-items: center;
    justify-content: center;
    gap: 64px;
  }
  .card {
    position: relative;
    width: 800px;
    height: 457px;
    border-radius: 28px;
    overflow: hidden;
  }
  .card--front { background: var(--paper); color: var(--ink); }
  .card--back { background: var(--navy); color: #fff; }

  /* front: contact column */
  .contact { position: absolute; left: 60px; top: 175px; width: 330px; }
  .firm-name {
    color: var(--sky);
    font-weight: 600;
    font-size: 26px;
    letter-spacing: 0.5px;
    white-space: nowrap;
    margin-bottom: 22px;
  }
  .contact-list { list-style: none; }
  .contact-item {
    display: flex;
    align-items: center;
    gap: 14px;
    font-size: 19px;
    font-weight: 500;
    white-space: nowrap;
    margin-bottom: 12px;
  }
  .contact-icon { width: 24px; height: 24px; flex: none; }
  .social-mark {
    width: 24px; height: 24px;
    background: var(--sky);
    border-radius: 5px;
    flex: none;
  }

  /* brand lockup */
  .brand {
    position: absolute;
    display: flex;
    flex-direction: column;
    align-items: center;
  }
  .brand-mark { border-radius: 50%; }
  .brand-name {
    font-weight: 700;
    letter-spacing: 2px;
    white-space: nowrap;
  }
  .brand-rule { height: 2px; }

  .card--front .brand { right: 50px; top: 70px; }
  .card--front .brand-mark { width: 80px; height: 80px; background: var(--navy); margin-bottom: 16px; }
  .card--front .brand-name { color: var(--navy); font-size: 36px; }
  .card--front .brand-rule { width: 300px; background: var(--sky); margin-top: 12px; }

  .band-sky {
    position: absolute; left: 0; bottom: 0;
    width: 62%; height: 12px; background: var(--sky);
  }
  .band-navy {
    position: absolute; right: 0; bottom: 0;
    width: 37%; height: 26px; background: var(--navy);
  }

  /* back */
  .card--back .brand { left: 0; right: 0; top: 90px; }
  .card--back .brand-mark { width: 120px; height: 120px; background: #fff; margin-bottom: 24px; }
  .card--back .brand-name { color: #fff; font-size: 56px; }
  .card--back .brand-rule { width: 440px; background: var(--sky); margin-top: 18px; }
  .band-accent {
    position: absolute; right: 0; bottom: 0;
    width: 42%; height: 28px; background: var(--sky);
  }
</style>
</head>
<body>

  <section class="card card--front">
    <div class="contact">
      <h1 class="firm-name">MARVELLA LAW PLLC</h1>
      <ul class="contact-list">
        <li class="contact-item">
          <svg class="contact-icon" viewBox="0 0 24 24" aria-hidden="true"><path fill="#1ab4ee" d="M6.6 10.8c1.4 2.8 3.8 5.1 6.6 6.6l2.2-2.2c.3-.3.7-.4 1-.2 1.1.4 2.3.6 3.6.6.6 0 1 .4 1 1V20c0 .6-.4 1-1 1C10.6 21 3 13.4 3 4c0-.6.4-1 1-1h3.5c.6 0 1 .4 1 1 0 1.2.2 2.4.6 3.6.1.3 0 .7-.2 1l-2.3 2.2z"/></svg>
          (555) 014-2290
        </li>
        <li class="contact-item">
          <svg class="contact-icon" viewBox="0 0 24 24" aria-hidden="true"><rect x="2" y="5" width="20" height="14" rx="1.5" fill="#1ab4ee"/><path d="M2.5 6 12 13l9.5-7" stroke="#fafafa" stroke-width="1.6" fill="none"/></svg>
          info@marvellalaw.com
        </li>
        <li class="contact-item">
          <svg class="contact-icon" viewBox="0 0 24 24" aria-hidden="true"><g fill="none" stroke="#1ab4ee" stroke-width="1.8"><circle cx="12" cy="12" r="10"/><ellipse cx="12" cy="12" rx="4.5" ry="10"/><path d="M2 12h20M4 7h16M4 17h16"/></g></svg>
          www.marvellalaw.com
        </li>
        <li class="contact-item">
          <span class="social-mark" aria-hidden="true"></span>
          /marvellalaw
        </li>
      </ul>
    </div>

    <div class="brand">
      <span class="brand-mark" aria-hidden="true"></span>
      <span class="brand-name">MARVELLA LAW</span>
      <span class="brand-rule"></span>
    </div>

    <span class="band-sky"></span>
    <span class="band-navy"></span>
  </section>

  <section class="card card--back">
    <div class="brand">
      <span class="brand-mark" aria-hidden="true"></span>
      <span class="brand-name">MARVELLA LAW</span>
      <span class="brand-rule"></span>
    </div>
    <span class="band-accent"></span>
  </section>

</body>
</html>
```